Mortgage Broker Site

Need a custom design for a mortgage broker site - please refer to the attached Word .doc that gives more detail.

Number of Pages Required

5+ page

Colors

Designer to choose colors to be used in the design.

```html
<!DOCTYPE html>
<html lang="en">
<head>
<meta charset="utf-8">
<title>Casera — Mortgage Refinance Loans</title>
<link href="https://fonts.googleapis.com/css2?family=Poppins:wght@400;500;600;700&family=Playfair+Display:wght@700;900&display=swap" rel="stylesheet">
<style>
:root{
  --wine:#9b0d22;
  --navy:#2d3f52;
  --ink:#1e1e1e;
  --grey:#7a7a7a;
  --hero-bg:#f4f3f5;
  --sky:#e6f4fb;
  --sand:#fbe3c4;
  --coral:#e8344f;
  --coral-dark:#d52a44;
  --footer:#2a2a2a;
  --white:#ffffff;
}
*{box-sizing:border-box;margin:0;padding:0}
html,body{width:684px;height:1200px;overflow:hidden}
body{position:relative;font-family:"Poppins",sans-serif;color:var(--ink);background:var(--white)}
.abs{position:absolute}

/* hero */
.hero{left:0;top:0;width:684px;height:302px;background:var(--hero-bg);overflow:hidden}
.hero-photo{left:280px;top:0;width:404px;height:302px;
  background:linear-gradient(90deg,var(--hero-bg) 0%,rgba(214,203,196,.6) 18%,#cdbfb4 40%,#8e7b70 62%,#4a4a52 80%,#d9d4d2 100%)}
.brand{left:80px;top:22px;display:flex;align-items:center;gap:5px;font-size:18px;font-weight:500;color:var(--ink)}
.brand-mark{width:9px;height:9px;background:var(--wine)}
.nav{left:210px;top:30px;font-size:7.3px;font-weight:500}
.nav a{color:var(--ink);text-decoration:none;position:absolute;top:0;white-space:nowrap}
.apply{left:460px;top:28px;width:59px;height:16px;border-radius:8px;background:var(--wine);color:var(--white);font-size:7.3px;font-weight:500;display:flex;align-items:center;justify-content:center}
.hero-title{left:82px;top:104px;font-family:"Playfair Display",serif;font-weight:900;font-size:25px;line-height:32px}
.hero-title .t1{color:var(--wine)}
.hero-title .t2{color:var(--navy)}
.hero-text{left:82px;top:176px;width:270px;font-size:8.6px;line-height:14px}
.btn{height:23px;border-radius:12px;color:var(--white);font-size:7px;font-weight:700;display:flex;align-items:center;justify-content:center;letter-spacing:.1px}
.btn-wine{left:83px;top:220px;width:91px;background:var(--wine)}
.btn-navy{left:185px;top:220px;width:93px;background:var(--navy)}

/* tools */
.tools-title{left:0;top:332px;width:684px;text-align:center;font-size:17px;font-weight:700}
.tools-title .w{color:var(--wine)} .tools-title .n{color:var(--navy)}
.tools-sub{left:192px;top:359px;width:300px;text-align:center;font-size:7.6px;line-height:13.5px;color:var(--grey)}
.card{top:402px;width:246px;height:160px;text-align:center}
.card-a{left:89px;background:var(--sky)}
.card-b{left:349px;background:var(--sand)}
.card-icon{position:absolute;left:96px;top:26px;width:54px;height:52px;border-radius:6px}
.card-a .card-icon{background:linear-gradient(135deg,#9fd3a0,#6f8a9c)}
.card-b .card-icon{background:linear-gradient(135deg,#e86a74,#c98aa8)}
.card h3{position:absolute;left:0;right:0;top:93px;font-size:11.5px;font-weight:600;color:#333}
.card p{position:absolute;left:20px;right:20px;top:114px;font-size:7.6px;line-height:13.5px;color:#555}

/* limits */
.limits{left:0;top:607px;width:684px;height:234px;background:#f3f2f4}
.limits-photo{left:0;top:607px;width:330px;height:234px;
  background:linear-gradient(90deg,#5a5452 0%,#a89a90 30%,#d9cfc6 60%,#efece9 85%,#f3f2f4 100%)}
.limits-pre{left:324px;top:658px;font-size:9.3px}
.limits-title{left:324px;top:670px;font-size:17.5px;font-weight:700;color:var(--wine);white-space:nowrap}
.limits-text{left:325px;top:703px;width:285px;font-size:7.5px;line-height:16px;color:#555}
.search{left:326px;top:764px;width:221px;height:31px;border:1px solid var(--wine);background:var(--white)}
.search span{position:absolute;left:14px;top:9px;font-size:8px;color:#888}
.search b{position:absolute;left:160px;top:3px;width:57px;height:23px;background:var(--wine);color:var(--white);font-size:7.5px;font-weight:600;display:flex;align-items:center;justify-content:center}

/* call band */
.band{left:0;top:841px;width:684px;height:205px;background:var(--coral)}
.town{left:0;top:955px;width:684px;height:91px;background:linear-gradient(180deg,var(--coral) 0%,var(--coral-dark) 40%,#c9263f 100%)}
.band-title{left:135px;top:890px;font-size:17px;line-height:22px;font-weight:700;color:var(--white)}
.phone{left:384px;top:895px;width:169px;height:40px;background:var(--wine);color:var(--white);display:flex;align-items:center;gap:14px;padding-left:16px;font-size:15px;font-weight:600}

/* footer */
.footer{left:0;top:1046px;width:684px;height:154px;background:var(--footer)}
.f-brand{left:90px;top:1090px;display:flex;align-items:center;gap:4px;font-size:15px;font-weight:500;color:var(--white)}
.f-brand i{width:7px;height:7px;background:var(--white)}
.social{top:1128px;width:12px;height:12px}
.copy{left:90px;top:1146px;font-size:5.6px;line-height:11px;color:var(--white)}
.col{top:1092px;color:var(--white)}
.col h4{font-size:8px;font-weight:600;margin-bottom:6px}
.col li{list-style:none;font-size:6.8px;line-height:13.8px;padding-left:1px}
</style>
</head>
<body>

<section class="abs hero">
  <div class="abs hero-photo" role="img" aria-label="Photo of a smiling agent holding house keys beside a happy family in a bright home"></div>
</section>
<div class="abs brand"><span>Casera</span><span class="brand-mark"></span></div>
<nav class="abs nav">
  <a href="#" style="left:0">Rates</a>
  <a href="#" style="left:37px">Purchase</a>
  <a href="#" style="left:89px">Refinance</a>
  <a href="#" style="left:142px">Schedule a Call</a>
  <a href="#" style="left:216px">Guide</a>
</nav>
<div class="abs apply">Apply Now</div>
<h1 class="abs hero-title"><span class="t1">Mortgage</span><br><span class="t2">Refinance Loans</span></h1>
<p class="abs hero-text">Lorem ipsum dolor sit amet, consectetur adipiscing elit, sed do eiusmod tempor incididunt ut labore et dolore</p>
<div class="abs btn btn-wine">PURCHASE RATES</div>
<div class="abs btn btn-navy">REFINANCE RATES</div>

<h2 class="abs tools-title"><span class="w">Mortgage</span> <span class="n">Tools</span></h2>
<p class="abs tools-sub">Lorem ipsum dolor sit amet, consectetur adipiscing elit, sed do eiusmod tempor incididunt ut labore et dolore</p>

<div class="abs card card-a">
  <div class="card-icon" role="img" aria-label="Illustration of a calculator beside a money bag"></div>
  <h3>Mortgage Calculator</h3>
  <p>See how much you can afford by home price, Monthly Payment, or Income</p>
</div>
<div class="abs card card-b">
  <div class="card-icon" role="img" aria-label="Illustration of a house with a receipt, coin and calculator"></div>
  <h3>Home Value Checker</h3>
  <p>Should you refinance? This calculator breaks down monthly and lifetime cost</p>
</div>

<section class="abs limits"></section>
<div class="abs limits-photo" role="img" aria-label="Photo of a couple reviewing mortgage papers next to a small wooden house model and coins"></div>
<p class="abs limits-pre">2019 Mortgage Loan Limits For</p>
<h2 class="abs limits-title">Conventional, FHA, &amp; VA Loans</h2>
<p class="abs limits-text">Mortgage loan limits for every U.S. county, as published by Northgate Home Finance &amp; Keystone Housing Trust, the Federal Housing Administration (FHA), and the Department of Veterans Affairs (VA)</p>
<div class="abs search"><span>your search...</span><b>SEARCH</b></div>

<section class="abs band"></section>
<div class="abs town" role="img" aria-label="Illustration of a row of town houses, trees and hot-air balloons in red tones"></div>
<h2 class="abs band-title">Connect with America’s<br>Lending Experts Today!</h2>
<div class="abs phone">
  <svg width="20" height="20" viewBox="0 0 24 24"><path d="M6.6 2.5l3 4-2 2.3a13 13 0 0 0 7.6 7.6l2.3-2 4 3-2.2 3.6C12 20.5 3.5 12 3 4.7z" fill="none" stroke="#fff" stroke-width="1.5" stroke-linejoin="round"/></svg>
  <span>(555) 014-2270</span>
</div>

<footer class="abs footer"></footer>
<div class="abs f-brand"><span>Casera</span><i></i></div>
<span class="abs social" style="left:90px;background:#3b5998"></span>
<span class="abs social" style="left:108px;background:#1da1f2"></span>
<span class="abs social" style="left:126px;background:#cb2027"></span>
<span class="abs social" style="left:144px;background:#f26522"></span>
<p class="abs copy">2009-2019 Copyright <b>Casera, Inc.</b><br>All rights reserved.</p>
<div class="abs col" style="left:241px"><h4>LINKS</h4><ul><li>Get a Mortgage Rate Now</li><li>Loan Types</li><li>Casera Disclosures</li><li>Conforming, VA &amp; FHA Loan Limits</li></ul></div>
<div class="abs col" style="left:389px"><h4>COMPANY</h4><ul><li>About Us</li><li>Careers</li><li>Casera Resources</li><li>Contact</li></ul></div>
<div class="abs col" style="left:502px"><h4>POLICIES</h4><ul><li>Security Policy</li><li>Privacy Policy</li><li>Terms of Use</li><li>Email Policy</li></ul></div>

</body>
</html>
```